Redesign a PPT into a more modern and appealing template, following the Brand Guidelines

Task Description: Redesign the PowerPoint presentation into a more modern and appealing template, ensuring adherence to the Brand Guidelines. Use the link below to acess the files:

https://kelvandrtpax-my.docsharebox.net/:f:/g/personal/marcelo_dorvanti_kelvandrtpax_cloudtenant_net/QxRk2pLmW94ZaoTr7ubjcnXE3yH5qqPwsuzgBVOK8h2JTd?e=LQp4tz

```html
<!DOCTYPE html>
<html lang="en">
<head>
<meta charset="utf-8">
<title>Kelvan Overview – Presentation Template</title>
<link href="https://fonts.googleapis.com/css2?family=Roboto:wght@400;500;700;900&family=Lato:wght@400;700&display=swap" rel="stylesheet">
<style>
:root{
  --green:#17693a;
  --red:#e31e24;
  --yellow:#fcc813;
  --dark:#3c3c3c;
  --ink:#222;
  --muted:#666;
  --bg:#e7e7e9;
  --white:#fff;
}
*{box-sizing:border-box;margin:0;padding:0}
html,body{width:1200px;height:940px;overflow:hidden;background:var(--bg);font-family:"Lato",sans-serif;color:var(--ink)}
.deck{position:relative;width:1200px;height:940px}
.slide{position:absolute;width:355px;height:200px;background:var(--white);overflow:hidden;box-shadow:0 2px 6px rgba(0,0,0,.18)}
.abs{position:absolute}
.title{position:absolute;left:10px;top:9px;font-family:"Roboto",sans-serif;font-weight:700;font-size:12.5px;color:var(--ink);line-height:1.1}
.title::after{content:"";display:block;width:16px;height:2px;background:var(--yellow);margin-top:5px}
.brand{position:absolute;right:10px;top:10px;display:flex;align-items:center;gap:2px;font-family:"Roboto",sans-serif;font-weight:700;font-size:7px;color:var(--ink)}
.brand i{display:block;width:6px;height:6px;border-radius:50%;background:var(--red)}
.footer{position:absolute;left:10px;right:10px;bottom:8px;height:12px}
.footer .dots{position:absolute;left:0;top:0;display:flex;gap:8px}
.footer .dots span{width:9px;height:9px;border-radius:50%;border:1.5px solid}
.footer .dots .g{border-color:var(--green);background:#cfe6d6}
.footer .dots .r{border-color:var(--red);background:#f9d2d3}
.footer .dots .y{border-color:var(--yellow);background:#fff3c4}
.footer .tag{position:absolute;left:0;top:9px;font-size:2.6px;font-weight:700;color:#333;letter-spacing:.1px}
.footer .rule{position:absolute;left:46px;right:6px;top:10px;height:0;border-top:.5px solid #999}
.footer .num{position:absolute;right:0;top:7px;font-size:3px;color:#333}
.small{font-size:4.6px;line-height:1.35;color:#444}
.photo{position:absolute;border-radius:1px}

/* cover */
.cover .topbar{left:30px;top:0;width:83px;height:7px;background:var(--green)}
.cover .logo{left:20px;top:38px;display:flex;align-items:center;gap:4px;font-family:"Roboto",sans-serif;font-weight:700;font-size:17px;color:var(--ink)}
.cover .logo i{display:block;width:14px;height:14px;border-radius:50%;background:var(--red)}
.cover .head{left:23px;top:92px;border-left:1.5px solid var(--ink);padding-left:5px;font-family:"Roboto",sans-serif;font-weight:900;font-size:20px;line-height:.95}
.cover .head .r{color:var(--red)}
.cover .place{left:23px;top:138px;font-size:9px;color:#333}
.cover .place sup{font-size:5px}
.cover .beads{left:23px;top:158px;display:flex;gap:4px}
.beads span{width:4px;height:4px;border-radius:50%}
.b-r{background:var(--red)}.b-y{background:var(--yellow)}.b-g{background:var(--green)}.b-k{background:var(--ink)}
.cover .web{left:23px;top:175px;font-size:7.5px;letter-spacing:2.6px;color:#222}

/* philosophy */
.pbox{position:absolute;top:68px;width:79px;height:94px;border:1.3px solid;text-align:center;font-family:"Roboto",sans-serif;font-weight:700;font-size:7px;line-height:1.2;padding:20px 4px 0}
.pbox .cap{position:absolute;left:-1.3px;right:-1.3px;top:-1.3px;height:11px;color:#fff;font-size:6.5px;line-height:11px}
.pbox.g{border-color:var(--green);color:var(--green)}.pbox.g .cap{background:var(--green)}
.pbox.r{border-color:var(--red);color:var(--red)}.pbox.r .cap{background:var(--red)}
.pbox.y{border-color:var(--yellow);color:var(--yellow)}.pbox.y .cap{background:var(--yellow)}

/* values */
.valbox{left:0;top:48px;width:140px;height:115px;background:var(--dark);color:#fff;font-size:5.8px;line-height:1.6;padding:5px 10px 0 18px}
.valbox .y{color:var(--yellow)}.valbox .r{color:var(--red)}
.vlabel{position:absolute;width:60px;font-size:3.3px;line-height:1.25;color:#666}
.vlabel b{display:block;color:var(--green);font-size:3.8px}

/* clients */
.ccard{position:absolute;top:44px;width:68px}
.ccard .photo{position:relative;width:68px;height:42px}
.ccard .lab{margin-top:6px;height:8px;color:#fff;font-size:4px;font-weight:700;text-align:center;line-height:8px}
.ccard p{margin-top:4px;font-size:3.6px;line-height:1.35;color:#555;text-align:justify}

/* sdg */
.sdg{position:absolute;left:37px;height:12px;width:270px}
.sdg .ic{position:absolute;left:0;top:0;width:12px;height:12px}
.sdg .nm{position:absolute;left:16px;top:2px;font-size:5px;font-weight:700;background:#fff;padding-right:1px}
.sdg .ln{position:absolute;left:16px;right:0;top:7px;border-top:.6px dotted #777}
.sdg .dot{position:absolute;top:3px;width:7px;height:7px;border-radius:50%;border:1.3px solid #fff;box-shadow:0 0 0 .6px #999}

/* impact */
.icol{left:22px;top:48px;width:132px;font-size:4.6px;line-height:1.45;color:#555;text-align:justify}
.icol p{margin-bottom:6px}
.icol b{color:#333}
.ibox{left:175px;top:45px;width:146px;height:112px;background:var(--dark);color:#fff;font-size:4.6px;line-height:1.45;padding:5px 5px;text-align:justify}
.ibox p{margin-bottom:6px}
.divider{left:164px;top:44px;height:114px;border-left:1.2px dotted var(--yellow)}

/* section */
.section{background:var(--dark)}
.section .band{left:0;right:0;top:152px;height:48px;background:#fff}
.section .h{left:0;right:0;top:55px;text-align:center;color:#fff;font-family:"Roboto",sans-serif;font-weight:900;line-height:.95}
.section .h .a{font-size:34px;display:block}
.section .h .b{font-size:25px;display:block;margin-top:3px}
.section .brand{color:#fff;top:14px;right:14px}

/* successes */
.stext{position:absolute;width:78px}
.stext b{display:block;font-size:4.8px;line-height:1.15;margin-bottom:2px}
.stext.r b{color:var(--red)}.stext.b b{color:#1f3f8f}.stext.c b{color:#1b8fb6}.stext.o b{color:#e35b13}
.stext span{font-size:3.4px;line-height:1.3;color:#666;display:block}

/* expansion */
.exp{position:absolute;top:45px;width:64px;text-align:center}
.exp .pill{margin:6px auto 0;height:10px;border-radius:5px;color:#fff;font-size:4.5px;line-height:10px;width:62px}
.exp p{margin-top:4px;font-size:3.6px;line-height:1.3;color:#333}
.exp .mini{display:flex;gap:2px;justify-content:center;margin-top:5px}
.exp .mini span{width:4px;height:4px;border-radius:50%}
</style>
</head>
<body>
<main class="deck">

<!-- 1 Cover -->
<section class="slide cover" style="left:52px;top:52px">
  <div class="abs topbar"></div>
  <div class="abs logo"><i></i>Kelvan</div>
  <h1 class="abs head"><span class="r">Kelvan</span><br>Overview</h1>
  <div class="abs place">Nampula, 29<sup>th</sup> January 2024</div>
  <div class="abs beads"><span class="b-r"></span><span class="b-y"></span><span class="b-g"></span><span class="b-k"></span><span class="b-r"></span><span class="b-y"></span><span class="b-g"></span><span class="b-k"></span></div>
  <div class="abs web">www.website.com</div>
  <div class="photo" role="img" aria-label="Portrait of a smiling woman in a red shirt and headscarf in front of a yellow radial dot pattern" style="left:165px;top:0;width:190px;height:200px;background:radial-gradient(circle at 70% 40%,#fff 0%,#fde38a 30%,#fcc813 55%,#fff 90%)"></div>
  <div class="photo" role="img" aria-label="Woman in red top" style="left:232px;top:40px;width:80px;height:160px;background:linear-gradient(180deg,#b36b3a 0%,#c8262c 35%,#a51d22 100%);border-radius:30px 30px 0 0;opacity:.85"></div>
</section>

<!-- 2 Milestones -->
<section class="slide" style="left:422px;top:52px">
  <h2 class="title">Milestones</h2>
  <div class="brand"><i></i>Kelvan</div>
  <svg class="abs" style="left:0;top:0" width="355" height="200" viewBox="0 0 355 200">
    <path d="M60 118 Q75 70 106 85 Q120 130 136 118 Q150 70 166 85 Q180 130 196 118 Q210 70 226 85 Q240 130 256 118 Q270 70 286 85" fill="none" stroke="#e8e8e8" stroke-width="12"/>
    <g stroke="#999" stroke-width=".5" stroke-dasharray="1.5 1.5">
      <line x1="75" y1="70" x2="75" y2="108"/><line x1="105" y1="70" x2="105" y2="74"/><line x1="135" y1="72" x2="135" y2="108"/>
      <line x1="165" y1="38" x2="165" y2="74"/><line x1="196" y1="72" x2="196" y2="108"/><line x1="226" y1="43" x2="226" y2="74"/>
      <line x1="256" y1="75" x2="256" y2="108"/><line x1="286" y1="43" x2="286" y2="74"/>
    </g>
    <g font-family="Roboto,sans-serif" font-weight="700" font-size="5.5" fill="#fff" text-anchor="middle">
      <circle cx="75" cy="118" r="10" fill="#e31e24"/><text x="75" y="120">2014</text>
      <circle cx="105" cy="84" r="10" fill="#fcc813"/><text x="105" y="86">2016</text>
      <circle cx="135" cy="118" r="10" fill="#17693a"/><text x="135" y="120">2017</text>
      <circle cx="165" cy="84" r="10" fill="#e31e24"/><text x="165" y="86" font-size="4">2019/20</text>
      <circle cx="196" cy="118" r="10" fill="#fcc813"/><text x="196" y="120">2021</text>
      <circle cx="226" cy="84" r="10" fill="#17693a"/><text x="226" y="86">2022</text>
      <circle cx="256" cy="118" r="10" fill="#e31e24"/><text x="256" y="120">2023</text>
      <circle cx="286" cy="84" r="10" fill="#fcc813"/><text x="286" y="86">2024</text>
      <circle cx="226" cy="112" r="6" fill="#17693a"/>
      <rect x="100" y="112" width="9" height="9" fill="#e31e24"/>
    </g>
    <g font-family="Lato,sans-serif" font-size="2.8" fill="#444" text-anchor="middle">
      <text x="75" y="58">Bank strategy shaped by</text><text x="75" y="62">lessons from micro-credit</text><text x="75" y="66">work in the north</text>
      <text x="135" y="63">Banking licence and start</text><text x="135" y="67">of operations</text>
      <text x="165" y="26">Shareholder strategy session</text><text x="165" y="30">with Brightmoor Capital</text><text x="165" y="34">capital raised to MZN 107.8 M</text>
      <text x="196" y="63">Break-even reached, 6,000</text><text x="196" y="67">clients, $1M portfolio</text>
      <text x="226" y="34">5-year anniversary</text><text x="226" y="38">growth and sustainability</text>
      <text x="256" y="66">Next phase: BSP 2023–2027</text><text x="256" y="70">expansion plan</text>
      <text x="286" y="34">Partnership to expand</text><text x="286" y="38">along the Nacala Corridor</text>
    </g>
    <text x="166" y="116" font-family="Lato,sans-serif" font-size="5" font-weight="700" fill="#2b3d7a" text-anchor="middle">Brightmoor</text>
  </svg>
  <div class="photo" role="img" aria-label="Group photo of clients in red outfits" style="left:62px;top:138px;width:60px;height:32px;background:linear-gradient(135deg,#c43a3a,#e8d7c7)"></div>
  <div class="photo" role="img" aria-label="Women dancing at a community event" style="left:129px;top:138px;width:50px;height:32px;background:linear-gradient(135deg,#a44a2c,#d9b08c)"></div>
  <div class="photo" role="img" aria-label="Meeting room with a strategy session" style="left:186px;top:138px;width:54px;height:32px;background:linear-gradient(135deg,#6d7c8a,#c9c4bd)"></div>
  <div class="photo" role="img" aria-label="Signing of a partnership agreement" style="left:247px;top:138px;width:50px;height:32px;background:linear-gradient(135deg,#aebccd,#e3e6ea)"></div>
  <div class="footer"><div class="dots"><span class="g"></span><span class="r"></span><span class="y"></span></div><div class="tag">Secure • Sustain • Grow</div><div class="rule"></div><div class="num">2</div></div>
</section>

<!-- 3 Philosophy -->
<section class="slide" style="left:790px;top:52px">
  <h2 class="title">Kelvan Philosophy</h2>
  <div class="brand"><i></i>Kelvan</div>
  <p class="abs small" style="left:11px;top:34px;width:320px;color:#666">Kelvan has been on the frontline among financial service providers in providing products and services with the main focus on poverty reduction efforts and other social advances in Mozambique specifically the northern region.</p>
  <div class="pbox g" style="left:36px"><div class="cap">OUR PURPOSE</div>Kelvan enables positive economic transformation for individuals and growing entrepreneurs in Mozambique.</div>
  <div class="pbox r" style="left:136px"><div class="cap">OUR VISION</div>Kelvan is the leading microfinance bank in Mozambique.</div>
  <div class="pbox y" style="left:236px"><div class="cap">OUR MISSION</div>Kelvan provides a range of financial solutions in an inclusive, simple, responsible, and sustainable manner.</div>
  <div class="footer"><div class="dots"><span class="g"></span><span class="r"></span><span class="y"></span></div><div class="tag">Secure • Sustain • Grow</div><div class="rule"></div><div class="num">3</div></div>
</section>

<!-- 4 Values -->
<section class="slide" style="left:52px;top:265px">
  <h2 class="title" style="font-size:12px">Values &amp; Business<br>Principles</h2>
  <div class="brand"><i></i>Kelvan</div>
  <div class="abs valbox">Our values are <span class="y">inclusive</span>, simple, <span class="r">responsible</span> an <span class="y">sustainable</span> in line with the principles of our shareholders the Alpine Development Agency (ADA) and Brightmoor Moçambique who are committed with Kelvan´s purpose and mission aligned with the financial inclusion policy of the Government of Mozambique.</div>
  <div class="abs" style="left:158px;top:22px;font-size:4.5px;color:#aaa;font-weight:700">KELVAN's Business Principles</div>
  <svg class="abs" style="left:205px;top:65px" width="80" height="80" viewBox="0 0 80 80">
    <g fill="none" stroke-width="11" transform="rotate(-90 40 40)">
      <circle cx="40" cy="40" r="26" stroke="#e31e24" stroke-dasharray="23.3 140"/>
      <circle cx="40" cy="40" r="26" stroke="#fcc813" stroke-dasharray="23.3 140" stroke-dashoffset="-23.3"/>
      <circle cx="40" cy="40" r="26" stroke="#17693a" stroke-dasharray="23.3 140" stroke-dashoffset="-46.6"/>
      <circle cx="40" cy="40" r="26" stroke="#17693a" stroke-dasharray="23.3 140" stroke-dashoffset="-69.9"/>
      <circle cx="40" cy="40" r="26" stroke="#17693a" stroke-dasharray="23.3 140" stroke-dashoffset="-93.2"/>
      <circle cx="40" cy="40" r="26" stroke="#e31e24" stroke-dasharray="23.3 140" stroke-dashoffset="-116.5"/>
      <circle cx="40" cy="40" r="26" stroke="#e31e24" stroke-dasharray="23.3 140" stroke-dashoffset="-139.8"/>
    </g>
    <circle cx="40" cy="40" r="17" fill="#fff" stroke="#ddd"/>
    <g fill="#17693a"><circle cx="34" cy="36" r="2.5"/><circle cx="40" cy="34" r="2.5"/><circle cx="46" cy="36" r="2.5"/><rect x="31" y="40" width="18" height="7" rx="3"/></g>
  </svg>
  <div class="vlabel" style="left:220px;top:38px;text-align:center"><b>Innovative Technologies</b>Innovative tech base for cost-efficient products</div>
  <div class="vlabel" style="left:160px;top:52px;text-align:right"><b>Continuous Product Development</b>Steady product work driven by client needs</div>
  <div class="vlabel" style="left:290px;top:52px"><b>Promoting Financial health and Client's Growth</b>Financial education that builds sustainability</div>
  <div class="vlabel" style="left:148px;top:100px;text-align:right"><b>Financial Inclusion</b>Adapted services for excluded groups and informal businesses</div>
  <div class="vlabel" style="left:290px;top:100px"><b>Transparent Client Communication</b>Open communication for trust-based relationships</div>
  <div class="vlabel" style="left:190px;top:140px;text-align:center"><b>Operational Sustainability</b>Lower costs and better efficiency</div>
  <div class="vlabel" style="left:250px;top:140px"><b>Talent Management</b>Recruiting and keeping motivated talent</div>
  <div class="footer"><div class="dots"><span class="g"></span><span class="r"></span><span class="y"></span></div><div class="tag">Secure • Sustain • Grow</div><div class="rule"></div><div class="num">4</div></div>
</section>

<!-- 5 Clients -->
<section class="slide" style="left:422px;top:265px">
  <h2 class="title">Kelvan Clients</h2>
  <div class="brand"><i></i>Kelvan</div>
  <div class="ccard" style="left:26px"><div class="photo" role="img" aria-label="Group of women micro-entrepreneurs" style="background:linear-gradient(135deg,#c0453a,#d9c2a8)"></div><div class="lab" style="background:var(--green)">Nano &amp; Micro-Entrepreneurs</div><p>• The primary beneficiaries of Kelvan's financial services and the main client segments in the Mozambican informal sector.<br><br>• With the majority being women, they are the driving force of local, dominantly informal trade.</p></div>
  <div class="ccard" style="left:104px"><div class="photo" role="img" aria-label="Shopkeeper in a small store" style="background:linear-gradient(135deg,#6b4a3a,#c9a27c)"></div><div class="lab" style="background:var(--red)">Small entrepreneurs</div><p>• Are a growing client segment that needs an increase in working capital to grow their slightly formalized businesses.<br><br>• These entrepreneurs face strong loan demand but cannot meet commercial banks' KYC requirements.</p></div>
  <div class="ccard" style="left:182px"><div class="photo" role="img" aria-label="Farmers working in a green field" style="background:linear-gradient(135deg,#4f7d3a,#a7c27a)"></div><div class="lab" style="background:var(--yellow)">Small farmers</div><p>• Are mostly excluded from formal financial services due to the perceived high risk of the nature of their business.<br><br>• They provide vital employment opportunities in rural areas beyond family members.</p></div>
  <div class="ccard" style="left:260px"><div class="photo" role="img" aria-label="Shop owner in front of a stocked store" style="background:linear-gradient(135deg,#c23b2f,#e3c56a)"></div><div class="lab" style="background:var(--dark)">Medium entrepreneurs</div><p>• With formalized successful businesses in larger-scale trade, manufacturing, transport and agriculture value chain economy, these firms express strong loan demand with minimal bureaucracy due to urgency.</p></div>
  <div class="footer"><div class="dots"><span class="g"></span><span class="r"></span><span class="y"></span></div><div class="tag">Secure • Sustain • Grow</div><div class="rule"></div><div class="num">5</div></div>
</section>

<!-- 6 SDG -->
<section class="slide" style="left:790px;top:265px">
  <h2 class="title">Social Development Impact</h2>
  <div class="brand"><i></i>Kelvan</div>
  <div class="abs" style="left:152px;top:34px;font-size:5px;font-weight:700;color:var(--red)">Specific target</div>
  <div class="abs" style="left:205px;top:34px;font-size:5px;font-weight:700;color:var(--ink)">Contribution</div>
  <div class="abs" style="left:250px;top:34px;font-size:5px;font-weight:700;color:var(--yellow)">Specific project</div>
  <div class="sdg" style="top:42px"><div class="ic" style="background:#e5243b"></div><div class="ln"></div><div class="nm" style="color:#e5243b">1 - No Poverty</div><div class="dot" style="left:131px;background:#f07b55"></div><div class="dot" style="left:181px;background:var(--green)"></div></div>
  <div class="sdg" style="top:58px"><div class="ic" style="background:#dda63a"></div><div class="ln"></div><div class="nm" style="color:#dda63a">2 - Zero Hunger</div><div class="dot" style="left:181px;background:var(--green)"></div></div>
  <div class="sdg" style="top:74px"><div class="ic" style="background:#4c9f38"></div><div class="ln"></div><div class="nm" style="color:#4c9f38">3 - Good health and well being</div><div class="dot" style="left:181px;background:var(--green)"></div></div>
  <div class="sdg" style="top:89px"><div class="ic" style="background:#c5192d"></div><div class="ln"></div><div class="nm" style="color:#c5192d">4 - Quality education</div><div class="dot" style="left:131px;background:#f07b55"></div><div class="dot" style="left:231px;background:var(--yellow)"></div></div>
  <div class="sdg" style="top:105px"><div class="ic" style="background:#ff3a21"></div><div class="ln"></div><div class="nm" style="color:#ff3a21">5 - Gender equality</div><div class="dot" style="left:131px;background:#f07b55"></div><div class="dot" style="left:181px;background:var(--green)"></div></div>
  <div class="sdg" style="top:121px"><div class="ic" style="background:#a21942"></div><div class="ln"></div><div class="nm" style="color:#a21942">8 - Decent work and economic growth</div><div class="dot" style="left:131px;background:#f07b55"></div><div class="dot" style="left:181px;background:var(--green)"></div></div>
  <div class="sdg" style="top:136px"><div class="ic" style="background:#dd1367"></div><div class="ln"></div><div class="nm" style="color:#dd1367">10 - Reduced inequalities</div><div class="dot" style="left:131px;background:#f07b55"></div><div class="dot" style="left:181px;background:var(--green)"></div></div>
  <div class="sdg" style="top:152px"><div class="ic" style="background:#19486a"></div><div class="ln"></div><div class="nm" style="color:#19486a">17 - Partnerships for the goals</div><div class="dot" style="left:131px;background:#f07b55"></div><div class="dot" style="left:181px;background:var(--green)"></div></div>
  <div class="footer"><div class="dots"><span class="g"></span><span class="r"></span><span class="y"></span></div><div class="tag">Secure • Sustain • Grow</div><div class="rule"></div><div class="num">6</div></div>
</section>

<!-- 7 Impact text -->
<section class="slide" style="left:52px;top:478px">
  <h2 class="title">Social Development Impact</h2>
  <div class="brand"><i></i>Kelvan</div>
  <div class="abs icol">
    <p>• Contribute to financial inclusion in <b>Northern Mozambique</b> by providing 45,055 loans to 20,350 microenterprises, indirectly impacting 101,750 livelihoods, with a majority (70%) of women.</p>
    <p>• Kelvan has <b>significantly influenced economic development</b> by effectively disbursing MZN 1,072,045,165 (CHF 14.5 million) in loans, leveraging Alpine public funds nearly 14 times the original investment of CHF 1 million. <b>This initiative has resulted in job creation, increases in income, and improvements in living conditions</b> for Kelvan's clients.</p>
    <p>• The bank achieved a <b>major recognition</b> in the Mozambican financial community by the entry of Brightmoor Moçambique in 2020.</p>
  </div>
  <div class="abs divider"></div>
  <div class="abs ibox">
    <p>• Kelvan is recognized as a <b>unique and leading employer in Nampula</b>, with a dedicated workforce of 95, half of whom are loan officers providing personalized services in Microfinance, upholding Kelvan's strong and positive image in the local employment landscape.</p>
    <p>• Kelvan has <b>achieved high productivity standards</b> with one loan officer managing 140 active clients on average. This is higher than the international standard of 120 clients.</p>
    <p>• Kelvan signed a loan agreement of US$ 2 Million with the Global Fund for Rural Growth (GFRG) <b>which is significant accreditation achievement in obtaining a quality seal.</b></p>
  </div>
  <div class="footer"><div class="dots"><span class="g"></span><span class="r"></span><span class="y"></span></div><div class="tag">Secure • Sustain • Grow</div><div class="rule"></div><div class="num">7</div></div>
</section>

<!-- 8 Active clients chart -->
<section class="slide" style="left:422px;top:478px">
  <h2 class="title">Kelvan in Figures</h2>
  <div class="brand"><i></i>Kelvan</div>
  <svg class="abs" style="left:0;top:0" width="355" height="200" viewBox="0 0 355 200" font-family="Lato,sans-serif">
    <text x="172" y="46" font-size="5" text-anchor="middle" fill="#555">EVOLUTION OF ACTIVE CLIENTS</text>
    <g font-size="3" fill="#333" text-anchor="end">
      <text x="56" y="53">14,000</text><text x="56" y="67">12,000</text><text x="56" y="81">10,000</text><text x="56" y="95">8,000</text>
      <text x="56" y="109">6,000</text><text x="56" y="123">4,000</text><text x="56" y="137">2,000</text><text x="56" y="151">0</text>
    </g>
    <text x="27" y="103" font-size="3" font-weight="700">Axis Title</text>
    <g>
      <rect x="72" y="140.5" width="11" height="9.5" fill="#17693a"/>
      <rect x="109" y="117.1" width="11" height="32.9" fill="#17693a"/><rect x="109" y="116.9" width="11" height=".2" fill="#e31e24"/>
      <rect x="146" y="104.6" width="11" height="45.4" fill="#17693a"/><rect x="146" y="102.2" width="11" height="2.4" fill="#e31e24"/>
      <rect x="183" y="114.6" width="11" height="35.4" fill="#17693a"/><rect x="183" y="101" width="11" height="13.6" fill="#e31e24"/>
      <rect x="220" y="111.2" width="11" height="38.8" fill="#17693a"/><rect x="220" y="83.6" width="11" height="27.6" fill="#e31e24"/>
      <rect x="257" y="112.2" width="11" height="37.8" fill="#17693a"/><rect x="257" y="73.9" width="11" height="38.3" fill="#e31e24"/>
      <rect x="294" y="111.2" width="11" height="38.8" fill="#17693a"/><rect x="294" y="56.9" width="11" height="54.3" fill="#e31e24"/>
    </g>
    <g font-size="5.5" fill="#333" text-anchor="middle">
      <text x="128" y="103">4 720</text><text x="151" y="96">6 829</text><text x="179" y="96">7 000</text>
      <text x="208" y="79">9 480</text><text x="248" y="70">10 869</text><text x="283" y="55">13 304</text>
    </g>
    <line x1="60" y1="110" x2="300" y2="38" stroke="#333" stroke-width=".4"/>
    <text x="186" y="74" font-size="4" transform="rotate(-17 186 74)">CAGR 46,2%</text>
    <line x1="60" y1="150" x2="320" y2="150" stroke="#ccc" stroke-width=".4"/>
    <g font-size="2.8" fill="#333" text-anchor="middle">
      <text x="77" y="154">Dec-17</text><text x="114" y="154">Dec-18</text><text x="151" y="154">Dec-19</text><text x="188" y="154">Dec-20</text><text x="225" y="154">Dec-21</text><text x="262" y="154">Dec-22</text><text x="299" y="154">Dec-23</text>
      <text x="114" y="159">26</text><text x="151" y="159">344</text><text x="188" y="159">1,944</text><text x="225" y="159">3,931</text><text x="262" y="159">5,468</text><text x="299" y="159">7,754</text>
      <text x="77" y="164">1,362</text><text x="114" y="164">4,694</text><text x="151" y="164">6,485</text><text x="188" y="164">5,056</text><text x="225" y="164">5,549</text><text x="262" y="164">5,401</text><text x="299" y="164">5,550</text>
    </g>
    <g font-size="2.8" fill="#333"><rect x="30" y="156" width="2" height="2" fill="#e31e24"/><text x="33" y="158">Voluntary Savers</text><rect x="30" y="161" width="2" height="2" fill="#17693a"/><text x="33" y="163">Active Borrowers</text></g>
    <g stroke="#e2e2e2" stroke-width=".3"><line x1="60" y1="155.5" x2="320" y2="155.5"/><line x1="60" y1="160.5" x2="320" y2="160.5"/><line x1="60" y1="165.5" x2="320" y2="165.5"/></g>
  </svg>
  <div class="footer"><div class="dots"><span class="g"></span><span class="r"></span><span class="y"></span></div><div class="tag">Secure • Sustain • Grow</div><div class="rule"></div><div class="num">8</div></div>
</section>

<!-- 9 Two charts -->
<section class="slide" style="left:790px;top:478px">
  <h2 class="title">Kelvan in Figures</h2>
  <div class="brand"><i></i>Kelvan</div>
  <svg class="abs" style="left:0;top:0" width="355" height="200" viewBox="0 0 355 200" font-family="Lato,sans-serif">
    <text x="92" y="50" font-size="5.5" fill="#555" text-anchor="middle">Chart Title</text>
    <text x="132" y="49" font-size="3" fill="#555">(in millions MZN)</text>
    <g font-size="2.5" fill="#555" text-anchor="end"><text x="14" y="58">250</text><text x="14" y="77">200</text><text x="14" y="95">150</text><text x="14" y="114">100</text><text x="14" y="132">50</text><text x="14" y="151">0</text></g>
    <g fill="#17693a">
      <rect x="20" y="146" width="12" height="4"/><rect x="42" y="134" width="12" height="16"/><rect x="64" y="127" width="12" height="23"/>
      <rect x="86" y="117" width="12" height="33"/><rect x="108" y="98" width="12" height="52"/><rect x="130" y="86" width="12" height="64"/><rect x="152" y="74" width="12" height="76"/>
    </g>
    <line x1="40" y1="140" x2="148" y2="62" stroke="#333" stroke-width=".4"/>
    <text x="83" y="110" font-size="3.8" transform="rotate(-36 83 110)">CAGR 6 0,9%</text>
    <g font-size="4" fill="#333" text-anchor="middle"><text x="26" y="156">Dec-17</text><text x="48" y="156">Dec-18</text><text x="70" y="156">Dec-19</text><text x="92" y="156">Dec-20</text><text x="114" y="156">Dec-21</text><text x="136" y="156">Dec-22</text><text x="158" y="156">Dec-23</text></g>

    <text x="250" y="50" font-size="4.5" fill="#333" text-anchor="middle">DEPOSIT PORTFOLIO GROWTH</text>
    <text x="307" y="49" font-size="3" fill="#555">(in millions MZN)</text>
    <g font-size="2.5" fill="#555" text-anchor="end"><text x="195" y="60">40</text><text x="195" y="72">35</text><text x="195" y="83">30</text><text x="195" y="95">25</text><text x="195" y="106">20</text><text x="195" y="118">15</text><text x="195" y="129">10</text><text x="195" y="140">5</text><text x="195" y="151">0</text></g>
    <g fill="#e31e24">
      <rect x="198" y="146" width="12" height="4"/><rect x="219" y="133" width="12" height="17"/><rect x="240" y="127" width="12" height="23"/>
      <rect x="261" y="101" width="12" height="49"/><rect x="282" y="102" width="12" height="48"/><rect x="303" y="87" width="12" height="63"/><rect x="324" y="71" width="12" height="79"/>
    </g>
    <line x1="198" y1="136" x2="318" y2="66" stroke="#333" stroke-width=".4"/>
    <text x="245" y="106" font-size="3.8" transform="rotate(-30 245 106)">CAGR 63,9%</text>
    <g font-size="4" fill="#333" text-anchor="middle"><text x="204" y="156">Dec-17</text><text x="225" y="156">Dec-18</text><text x="246" y="156">Dec-19</text><text x="267" y="156">Dec-20</text><text x="288" y="156">Dec-21</text><text x="309" y="156">Dec-22</text><text x="330" y="156">Dec-23</text></g>
  </svg>
  <div class="footer"><div class="dots"><span class="g"></span><span class="r"></span><span class="y"></span></div><div class="tag">Secure • Sustain • Grow</div><div class="rule"></div><div class="num">9</div></div>
</section>

<!-- 10 Section -->
<section class="slide section" style="left:52px;top:690px">
  <div class="photo" role="img" aria-label="Yellow radial dot pattern in the top-left corner" style="left:0;top:0;width:75px;height:70px;background:radial-gradient(circle at 0 0,#fcc813 0%,#fcc813 45%,rgba(252,200,19,0) 75%)"></div>
  <div class="photo" role="img" aria-label="Faint grey dot pattern at lower right" style="left:290px;top:90px;width:65px;height:62px;background:radial-gradient(circle at 100% 100%,#5a5a5a 0%,rgba(90,90,90,0) 70%)"></div>
  <div class="brand"><i></i>Kelvan</div>
  <h2 class="abs h"><span class="a">Ajustamentos</span><span class="b">Estratégicos</span></h2>
  <div class="abs band"></div>
  <div class="abs beads" style="left:8px;top:168px;display:flex;gap:4.5px">
    <span class="b-r"></span><span class="b-y"></span><span class="b-g"></span><span class="b-k"></span><span class="b-r"></span><span class="b-y"></span><span class="b-g"></span><span class="b-k"></span><span class="b-r"></span><span class="b-y"></span><span class="b-g"></span><span class="b-k"></span><span class="b-r"></span><span class="b-y"></span><span class="b-g"></span><span class="b-k"></span><span class="b-r"></span><span class="b-y"></span><span class="b-g"></span><span class="b-k"></span><span class="b-r"></span><span class="b-y"></span><span class="b-g"></span><span class="b-k"></span><span class="b-r"></span><span class="b-y"></span><span class="b-g"></span><span class="b-k"></span><span class="b-r"></span><span class="b-y"></span><span class="b-g"></span><span class="b-k"></span><span class="b-r"></span><span class="b-y"></span><span class="b-g"></span><span class="b-k"></span><span class="b-r"></span><span class="b-y"></span><span class="b-g"></span><span class="b-k"></span>
  </div>
</section>

<!-- 11 Successes -->
<section class="slide" style="left:422px;top:690px">
  <h2 class="title">Sucessos Estratégicos</h2>
  <div class="brand"><i></i>Kelvan</div>
  <div class="stext r" style="left:26px;top:44px"><b>Ability to Manage Crises and Adapt</b><span>Maintenance of focus on operational efficiency and customer satisfaction.</span></div>
  <div class="stext b" style="left:26px;top:82px"><b>Contribution to the Agricultural Sector and Inclusion</b><span>Disbursement of approximately 83.5 million meticais in the productive chain of the agricultural sector</span></div>
  <div class="stext c" style="left:26px;top:122px"><b>Crescimento Sustentável – Aumento dos Depósitos Voluntários</b><span>There was a 42% increase in the number of savers and a 60% increase in deposit volume, totaling 7,754 saving clients.</span></div>
  <div class="stext r" style="left:255px;top:42px"><b>Internship Program - Talent Retention</b><span>Resulted in the hiring of 10 interns, with 80% being women.</span></div>
  <div class="stext r" style="left:255px;top:78px"><b>Establishment of the Recovery Department - Enhancement of the Collection Strategy</b><span>Composta por 5 profissionais, incluindo uma supervisora.</span></div>
  <div class="stext o" style="left:255px;top:122px"><b>Aprimoramento do Conhecimento do Mercado Local - Enfoque nas Zonas Agrícolas</b><span>Alocação de um oficial exclusivo para atuar nas zonas agrícolas</span></div>
  <svg class="abs" style="left:118px;top:30px" width="126" height="126" viewBox="0 0 126 126">
    <circle cx="63" cy="63" r="42" fill="none" stroke="#eee" stroke-width="8"/>
    <circle cx="63" cy="63" r="16" fill="#fff" stroke="#eee" stroke-width="1.5"/>
    <text x="63" y="65" font-family="Roboto,sans-serif" font-weight="700" font-size="6" fill="#222" text-anchor="middle">Kelvan</text>
    <g fill="#fff" stroke-width="2.2">
      <circle cx="63" cy="16" r="11" stroke="#e5246b"/><circle cx="98" cy="31" r="11" stroke="#e35b13"/>
      <circle cx="108" cy="70" r="11" stroke="#fcc813"/><circle cx="82" cy="104" r="11" stroke="#8bc34a"/>
      <circle cx="44" cy="104" r="11" stroke="#1aa08a"/><circle cx="18" cy="70" r="11" stroke="#2a6cc7"/>
      <circle cx="28" cy="31" r="11" stroke="#7a3fa0"/>
    </g>
    <g fill="none" stroke="#666" stroke-width=".8">
      <circle cx="63" cy="16" r="4"/><rect x="95" y="27" width="6" height="8"/><rect x="104" y="67" width="8" height="6"/>
      <path d="M78 106 h8 l-2 -4 h-4z"/><rect x="40" y="101" width="8" height="6"/><path d="M14 74 v-6 M17 74 v-8 M20 74 v-5 M23 74 v-7"/><path d="M25 34 h6 M28 27 v7"/>
    </g>
  </svg>
  <div class="stext" style="left:118px;top:156px;width:130px"><b style="color:var(--green)">Melhoria das Formações em Literacia Financeira</b><span>Treinamento a 2.714 potenciais clientes, 1.694 mulheres e 1.004 homens. 1.871 com acesso ao financiamento 467 com contas poupanças</span></div>
  <div class="footer"><div class="dots"><span class="g"></span><span class="r"></span><span class="y"></span></div><div class="tag">Secure • Sustain • Grow</div><div class="rule"></div><div class="num">11</div></div>
</section>

<!-- 12 Expansion -->
<section class="slide" style="left:790px;top:690px">
  <h2 class="title">Expansion Plan</h2>
  <div class="brand"><i></i>Kelvan</div>
  <div class="exp" style="left:28px">
    <svg width="44" height="44" viewBox="0 0 44 44"><circle cx="22" cy="22" r="17" fill="none" stroke="#17693a" stroke-width="7"/><text x="22" y="21" font-size="5.5" font-family="Roboto,sans-serif" font-weight="700" text-anchor="middle">100</text><text x="22" y="27" font-size="5" text-anchor="middle" font-family="Roboto,sans-serif" font-weight="700">%</text></svg>
    <div class="pill" style="background:var(--green)">Definition of Leadership</div>
    <p>Kelvan identified an experienced leader for the expansion process. It ran a market survey to gather local knowledge and relevant insights.</p>
    <div class="mini"><span class="b-r"></span><span class="b-y"></span><span class="b-g"></span></div>
  </div>
  <div class="exp" style="left:101px">
    <svg width="44" height="44" viewBox="0 0 44 44"><circle cx="22" cy="22" r="17" fill="none" stroke="#3c3c3c" stroke-width="7"/><text x="22" y="21" font-size="5.5" font-family="Roboto,sans-serif" font-weight="700" text-anchor="middle">100</text><text x="22" y="27" font-size="5" text-anchor="middle" font-family="Roboto,sans-serif" font-weight="700">%</text></svg>
    <div class="pill" style="background:var(--dark)">Hiring Local Interns</div>
    <p>Kelvan hired 4 client officers in February 2024, who were trained intensively in credit and financial literacy for 2 months.</p>
    <div class="mini"><span class="b-r"></span><span class="b-y"></span><span class="b-g"></span></div>
  </div>
  <div class="exp" style="left:174px">
    <svg width="44" height="44" viewBox="0 0 44 44"><circle cx="22" cy="22" r="17" fill="none" stroke="#fcc813" stroke-width="7"/><text x="22" y="21" font-size="5.5" fill="#fcc813" font-family="Roboto,sans-serif" font-weight="700" text-anchor="middle">100</text><text x="22" y="27" font-size="5" fill="#fcc813" text-anchor="middle" font-family="Roboto,sans-serif" font-weight="700">%</text></svg>
    <div class="pill" style="background:var(--yellow)">Financial Literacy</div>
    <p>By April 2024, more than 1,244 clients were trained in financial literacy, resulting in about 700 credit clients.</p>
    <div class="mini"><span class="b-r"></span><span class="b-y"></span><span class="b-g"></span></div>
  </div>
  <div class="exp" style="left:247px">
    <svg width="44" height="44" viewBox="0 0 44 44"><circle cx="22" cy="22" r="17" fill="none" stroke="#e31e24" stroke-width="7"/><text x="22" y="21" font-size="5.5" fill="#e31e24" font-family="Roboto,sans-serif" font-weight="700" text-anchor="middle">100</text><text x="22" y="27" font-size="5" fill="#e31e24" text-anchor="middle" font-family="Roboto,sans-serif" font-weight="700">%</text></svg>
    <div class="pill" style="background:var(--red)">Pilot Disbursements</div>
    <p>Kelvan ran pilot disbursements using M-Wallet for more than 983 clients, with a portfolio of 670 clients totalling 9.7 million meticais.</p>
    <div class="mini"><span class="b-r"></span><span class="b-y"></span><span class="b-g"></span></div>
  </div>
  <div class="footer"><div class="dots"><span class="g"></span><span class="r"></span><span class="y"></span></div><div class="tag">Secure • Sustain • Grow</div><div class="rule"></div><div class="num">11</div></div>
</section>

</main>
</body>
</html>
```